Dorian Walsby Psychotherapy Business Card Design Project

I need a welcoming business card for a Somatic Psychotherapy private practice based in Melbourne, Australia. I help individual clients to work through issues in their life that are inhibiting achieving their full potential. I would like a san serif font and the oculars are:
blue: R:37 G:61 B:95 C:93 M:77 Y:38 K:28
orange: R:241 G:103 B:43 C:0 M:74 Y:93 K:0
The final design should communicate warm, welcoming and safe environment in which clients are supported to grow. It should also convey a collaborative approach to achieve success between me (the therapist) and the client. The uploaded file is my new logo. Also an organic look and feel while maintaining professionalism and a clean, simple look is sought after.
In addition to the logo my details are:
Dorian Walsby
Psychotherapist
B.Arts., Grad Dip. T&D., Dip.Som.Psych, MRKTA, MLOHVB
0417 582 930
dwalsby@dorianwalsby.com.au
www.dorianwalsby.com.au
Target Market(s)
Psychotherapy Clients
Industry/Entity Type
Environment

```html
<!DOCTYPE html>
<html lang="en">
<head>
<meta charset="utf-8">
<title>Dorian Walsby Psychotherapy – Business Card</title>
<link href="https://fonts.googleapis.com/css2?family=Montserrat:wght@400;500;600;700&display=swap" rel="stylesheet">
<style>
  :root {
    --navy: #253d5f;
    --orange: #f1672b;
    --ink: #3a3a3a;
    --paper: #ffffff;
    --backdrop: #eceae6;
  }
  * { margin: 0; padding: 0; box-sizing: border-box; }
  html, body {
    width: 1200px; height: 398px; overflow: hidden;
    background: var(--backdrop);
    font-family: "Montserrat", Arial, sans-serif;
  }
  .stage { position: relative; width: 1200px; height: 398px; }
  .card {
    position: absolute; width: 511px; height: 292px;
    background: var(--paper); overflow: hidden;
    box-shadow: 0 1px 3px rgba(0,0,0,.25);
  }
  .card--front { left: 62px; top: 48px; }
  .card--back { left: 614px; top: 53px; }

  .brand-name {
    position: absolute; color: var(--navy);
    font-size: 26px; font-weight: 600; line-height: 1; white-space: nowrap;
  }
  .card--front .brand-name { left: 28px; top: 66px; }
  .card--back .brand-name { left: 0; right: 0; top: 128px; text-align: center; }

  .contact-band {
    position: absolute; left: 0; right: 0; top: 218px; bottom: 0;
    background: linear-gradient(100deg, var(--orange) 0%, var(--navy) 38%, var(--navy) 100%);
  }

  .person { position: absolute; left: 27px; top: 156px; color: var(--navy); }
  .person__name { font-size: 15px; font-weight: 700; }
  .person__role { font-size: 12px; font-weight: 500; }
  .person__creds { margin-top: 9px; font-size: 9px; color: var(--ink); letter-spacing: .1px; }

  .contact {
    position: absolute; right: 14px; top: 224px;
    list-style: none; text-align: right; color: var(--paper);
    font-size: 12.5px; line-height: 22px;
  }
  .contact li { display: flex; justify-content: flex-end; align-items: center; gap: 8px; }
  .contact svg { width: 10px; height: 10px; flex: none; }

  .web-line {
    position: absolute; left: 0; right: 0; top: 262px; text-align: center;
    font-size: 12px; letter-spacing: 3px; color: var(--ink);
  }
</style>
</head>
<body>
<div class="stage">

  <section class="card card--front">
    <p class="brand-name">Dorian Walsby Psychotherapy</p>

    <div class="person">
      <p><span class="person__name">Dorian Walsby ,</span> <span class="person__role">Psychotherapist</span></p>
      <p class="person__creds">B.Arts., Grad Dip. T&amp;D., Dip.Som.Psych, MRKTA, MLOHVB</p>
    </div>

    <div class="contact-band" role="img" aria-label="Decorative navy and orange flowing band"></div>

    <ul class="contact">
      <li>0417 582 930
        <svg viewBox="0 0 10 10" aria-hidden="true"><path d="M2,1 L4,1 L4.6,3 L3.5,3.8 C4,5 5,6 6.2,6.5 L7,5.4 L9,6 L9,8 C9,8.6 8.5,9 8,9 C4,9 1,6 1,2 C1,1.5 1.4,1 2,1 Z" fill="var(--paper)"/></svg>
      </li>
      <li>dwalsby@dorianwalsby.com.au
        <svg viewBox="0 0 10 10" aria-hidden="true"><rect x="0.5" y="2" width="9" height="6.5" fill="var(--paper)"/><path d="M0.5,2 L5,5.5 L9.5,2" fill="none" stroke="var(--navy)" stroke-width="0.8"/></svg>
      </li>
      <li>www.dorianwalsby.com.au
        <svg viewBox="0 0 10 10" aria-hidden="true"><circle cx="5" cy="5" r="4.2" fill="none" stroke="var(--paper)" stroke-width="1"/><ellipse cx="5" cy="5" rx="1.8" ry="4.2" fill="none" stroke="var(--paper)" stroke-width="0.8"/><path d="M0.8,5 H9.2" stroke="var(--paper)" stroke-width="0.8"/></svg>
      </li>
    </ul>
  </section>

  <section class="card card--back">
    <p class="brand-name">Dorian Walsby Psychotherapy</p>
    <p class="web-line">www.dorianwalsby.com.au</p>
  </section>

</div>
</body>
</html>
```